web page layout, style , color, font & flow design

We are developing a single page application. The SPA (single page application) will display natural gas pipeline flow data once the customer logs on. The customer has a choice of the region, the pipeline, the zone on the pipeline, whether the point is a delivery point or receipt point and the state the pipeline flows through.
we have jumpstarted the project and are attaching a pdf of the same.

we are using mockingbird for the wireframe. any designer is free to use this tool to make changes.

A mockingbird wireframe link is added below. you are free to use it and to make changes. please save the changed wireframe in a different name

we are looking for inputs on layout, style , color, font & flow.

A logo jpg file has also been attached.

Target Market(s)

this single web page is going to be used by natural gas traders and schedulers day in and day out. the application is more of business to business corporate application.

Industry/Entity Type

Delivery

Requirements
Must have
• layout ,flow, size, color, font , ease of use.

```html
<!DOCTYPE html>
<html lang="en">
<head>
<meta charset="utf-8">
<title>Fuelgrid – Wholesale NG Supply Analysis</title>
<link rel="stylesheet" href="https://fonts.googleapis.com/css2?family=Arimo:wght@400&family=Open+Sans:wght@300&display=swap">
<style>
  :root {
    --header-top: #f4f5f7;
    --header-bottom: #dfe2e6;
    --brand-blue: #0a52a3;
    --tab-grey: #8c8c8c;
    --tab-active-text: #0a52a3;
    --nav-green: #8dc63f;
    --nav-green-active: #6aab12;
    --table-orange: #f26a22;
    --row-light: #fdf2ed;
    --row-dark: #fce4da;
    --select-grey: #e5e5e5;
    --select-arrow: #8a8a8a;
    --text-dark: #333333;
    --text-title: #3d3d3d;
    --footer-bg: #e9edf0;
    --white: #ffffff;
  }
  * { box-sizing: border-box; margin: 0; padding: 0; }
  html, body { width: 1200px; height: 793px; overflow: hidden; }
  body {
    position: relative;
    background: var(--white);
    font-family: "Arimo", Arial, sans-serif;
    color: var(--text-dark);
  }

  .site-header {
    position: absolute; left: 0; top: 0; width: 1200px; height: 159px;
    background: linear-gradient(180deg, var(--header-top), var(--header-bottom));
  }
  .brand {
    position: absolute; left: 28px; top: 58px;
    display: flex; align-items: center; gap: 10px;
    font-size: 26px; color: var(--brand-blue);
  }
  .brand-dot {
    width: 34px; height: 34px; border-radius: 50%;
    background: var(--brand-blue);
  }
  .app-title {
    position: absolute; left: 206px; top: 55px;
    font-family: "Open Sans", Arial, sans-serif; font-weight: 300;
    font-size: 33px; color: var(--text-title); letter-spacing: 0.2px;
  }

  .main-nav {
    position: absolute; left: 0; top: 159px; width: 1200px; height: 49px;
    background: var(--brand-blue);
  }
  .region-tabs { position: absolute; left: 17px; top: 11px; display: flex; gap: 2.5px; list-style: none; }
  .region-tab {
    width: 124px; height: 38px; background: var(--tab-grey); color: var(--white);
    font-size: 17px; display: flex; align-items: center; justify-content: center;
  }
  .region-tab.is-active { background: var(--white); color: var(--tab-active-text); }
  .user-tools { position: absolute; right: 14px; top: 6px; display: flex; gap: 24px; }
  .user-tool { display: flex; flex-direction: column; align-items: center; color: var(--white); font-size: 11px; }
  .user-tool svg { width: 24px; height: 24px; margin-bottom: 2px; }

  .pipeline-list {
    position: absolute; left: 17px; top: 231px; width: 289px; list-style: none;
  }
  .pipeline-item {
    height: 33.3px; margin-bottom: 1px; background: var(--nav-green); color: var(--white);
    font-size: 17px; padding-left: 16px; display: flex; align-items: center;
  }
  .pipeline-item.is-active { background: var(--nav-green-active); }

  .content { position: absolute; left: 339px; top: 227px; width: 828px; }
  .breadcrumb { font-size: 21px; color: var(--text-title); }

  .filters { position: absolute; top: 52px; left: 1px; }
  .filter { position: absolute; top: 0; width: 135px; }
  .filter-select {
    height: 26px; background: var(--select-grey); position: relative;
    font-size: 15px; padding-left: 10px; line-height: 26px; color: var(--text-dark);
  }
  .filter-select::after {
    content: ""; position: absolute; right: 0; top: 0; width: 25px; height: 26px;
    background: var(--select-arrow);
  }
  .filter-select svg { position: absolute; right: 7px; top: 10px; width: 11px; height: 7px; z-index: 1; }
  .filter-hint { font-size: 11px; margin-top: 10px; white-space: nowrap; color: var(--text-dark); }

  .flow-table {
    position: absolute; left: 0; top: 132px; width: 828px;
    border-collapse: collapse; table-layout: fixed; font-size: 15px;
  }
  .flow-table th {
    background: var(--table-orange); color: var(--white); font-weight: 400;
    height: 37px; text-align: left; padding-left: 12px;
  }
  .flow-table td { height: 38px; padding-left: 12px; border-top: 1px solid var(--white); }
  .flow-table tbody tr:nth-child(odd) td { background: var(--row-light); }
  .flow-table tbody tr:nth-child(even) td { background: var(--row-dark); }

  .site-footer {
    position: absolute; left: 0; top: 689px; width: 1200px; height: 64px;
    background: var(--footer-bg); font-size: 14.5px; padding-left: 20px; line-height: 64px;
    color: var(--text-dark);
  }
</style>
</head>
<body>
  <header class="site-header">
    <div class="brand"><span class="brand-dot"></span>Fuelgrid</div>
    <h1 class="app-title">Wholesale NG Supply Analysis</h1>
  </header>

  <nav class="main-nav">
    <ul class="region-tabs">
      <li class="region-tab is-active">NorthEast</li>
      <li class="region-tab">MideWest</li>
      <li class="region-tab">SouthEast</li>
      <li class="region-tab">SouthWest</li>
      <li class="region-tab">Central</li>
      <li class="region-tab">West</li>
    </ul>
    <div class="user-tools">
      <div class="user-tool">
        <svg viewBox="0 0 24 24"><circle cx="12" cy="7" r="5.5" fill="#fff"/><path d="M2 23c0-6 4.5-9 10-9s10 3 10 9z" fill="#fff"/></svg>
        profile
      </div>
      <div class="user-tool">
        <svg viewBox="0 0 24 24"><g fill="#fff"><circle cx="12" cy="12" r="7.5"/><rect x="10" y="1" width="4" height="22" rx="1"/><rect x="1" y="10" width="22" height="4" rx="1"/><rect x="10" y="1" width="4" height="22" rx="1" transform="rotate(45 12 12)"/><rect x="10" y="1" width="4" height="22" rx="1" transform="rotate(-45 12 12)"/></g><circle cx="12" cy="12" r="3.5" fill="#0a52a3"/></svg>
        settings
      </div>
    </div>
  </nav>

  <ul class="pipeline-list">
    <li class="pipeline-item">Alderbrook</li>
    <li class="pipeline-item is-active">CRT</li>
    <li class="pipeline-item">Dunmore</li>
    <li class="pipeline-item">Eastern Bay NG</li>
    <li class="pipeline-item">East Ridge NG</li>
    <li class="pipeline-item">Emberline Gas</li>
    <li class="pipeline-item">Equiline Inc</li>
    <li class="pipeline-item">Slate Hill Gas</li>
    <li class="pipeline-item">Ironwood</li>
    <li class="pipeline-item">Harbors &amp; North East</li>
    <li class="pipeline-item">Milestone Pipeline</li>
    <li class="pipeline-item">Northfield Gas Supply Corp</li>
  </ul>

  <main class="content">
    <h2 class="breadcrumb" style="font-weight:400">NorthEast » CRT</h2>

    <div class="filters">
      <div class="filter" style="left:0">
        <div class="filter-select">updates<svg viewBox="0 0 11 7"><path d="M0 0h11L5.5 7z" fill="#fff"/></svg></div>
        <p class="filter-hint">Lorem, Ipsum, Dolor</p>
      </div>
      <div class="filter" style="left:195px">
        <div class="filter-select">location type<svg viewBox="0 0 11 7"><path d="M0 0h11L5.5 7z" fill="#fff"/></svg></div>
        <p class="filter-hint">Receipt, Delivery, Storage</p>
      </div>
      <div class="filter" style="left:390px">
        <div class="filter-select">states<svg viewBox="0 0 11 7"><path d="M0 0h11L5.5 7z" fill="#fff"/></svg></div>
        <p class="filter-hint">Interstate pipeline</p>
      </div>
      <div class="filter" style="left:584px">
        <div class="filter-select">zones<svg viewBox="0 0 11 7"><path d="M0 0h11L5.5 7z" fill="#fff"/></svg></div>
        <p class="filter-hint">pipeline zones</p>
      </div>
    </div>

    <table class="flow-table">
      <colgroup>
        <col style="width:81px"><col style="width:93px"><col style="width:110px"><col style="width:96px">
        <col style="width:93px"><col style="width:93px"><col style="width:112px"><col style="width:150px">
      </colgroup>
      <thead>
        <tr><th>gasday</th><th>location</th><th>loc_name</th><th>flow_ind</th><th>loc_desc</th><th>op_cap</th><th>sch_cap</th><th>op_avail_cap</th></tr>
      </thead>
      <tbody>
        <tr><td>item 3</td><td>item 4</td><td></td><td></td><td></td><td></td><td></td><td></td></tr>
        <tr><td>item 5</td><td>item 6</td><td></td><td></td><td></td><td></td><td></td><td></td></tr>
        <tr><td>item 3</td><td>item 4</td><td></td><td></td><td></td><td></td><td></td><td></td></tr>
        <tr><td>item 5</td><td>item 6</td><td></td><td></td><td></td><td></td><td></td><td></td></tr>
      </tbody>
    </table>
  </main>

  <footer class="site-footer">Fuelgrid Wholesale NG Supply Analysis</footer>
</body>
</html>
```